Lanternway 7.5 - Educational Guide/Course-pack/Worksheet

Our Lanternway 7.5 toolkit is an educational workshop that focuses on inspiring student initiatives in the classroom! We need a new educational course guide or course-pack for students/teachers that clearly outlines or explains the program steps, offers helpful tips and includes empty spaces/lines where their can write down their great ideas or notes. This will include a;

- Teachers Guide (1 Page)
- Student Guide/Worksheet (4 Pages)
- Group Pack Resources (3 Pages)

This will consist of designing/formatting text, stock animation/icons, font, etc. We have included our new logo (color, branding, etc.) and all of the text for each separate course-pack. We have also attached our new website to give you an idea of the program style.

Our workshop can be for any school project like Technology, Community, Environment, Art, Science, etc.

Target Market(s)

High School Students/Teachers

Industry/Entity Type

Education

Font styles to use
Sans Serif

Colors
f68e4e
acd037
34a7d8

Requirements
Must have
• Use our brand colors from logo.
Should not have
• Should not be too childish.

```html
<!DOCTYPE html>
<html lang="en">
<head>
<meta charset="utf-8">
<title>Lanternway 7.5 Course-Pack</title>
<link href="https://fonts.googleapis.com/css2?family=Open+Sans:wght@400;600;700;800&family=Oswald:wght@500;700&display=swap" rel="stylesheet">
<style>
:root{
  --teal:#2f9b90;
  --teal-dark:#23786f;
  --mint:#7de6bb;
  --cream:#fbf7d8;
  --ink:#12332f;
  --white:#ffffff;
  --orange:#f68e4e;
  --green:#acd037;
  --blue:#34a7d8;
  --purple:#8a4fd8;
}
*{box-sizing:border-box;margin:0;padding:0}
html,body{width:1200px;height:934px;overflow:hidden;background:#fff}
body{position:relative;font-family:"Open Sans",Arial,sans-serif;color:var(--white)}
.page-number{position:absolute;font-size:44px;line-height:1;color:#000;width:60px;text-align:center}
.page{position:absolute;background:var(--teal);overflow:hidden;font-size:5px;line-height:1.35}
.abs{position:absolute}
.art{position:absolute;border-radius:2px}
.h-sec{font-weight:700;font-size:8px;text-decoration:underline;text-align:center}
.h-sub{font-weight:700;font-size:7px}
.rule{border-bottom:0.6px solid rgba(255,255,255,.8);height:7px}
.dark .rule{border-bottom-color:rgba(18,51,47,.7)}
.dark{color:var(--ink)}
.mint-box{position:absolute;background:var(--mint);color:var(--ink);padding:3px;font-size:4.6px;line-height:1.3;border:0.6px solid rgba(255,255,255,.6)}
.mint-box b{display:block;text-decoration:underline;margin-bottom:2px;font-size:5px}
.brand{position:absolute;display:flex;align-items:center;gap:7px}
.brand-dot{width:22px;height:22px;border-radius:50%;background:var(--orange)}
.brand-name{font-weight:700;font-size:15px;color:var(--white);line-height:1}
table{border-collapse:collapse;width:100%}
td,th{border:0.6px solid var(--teal-dark);font-size:4.8px;padding:1px 2px;height:8px;color:var(--ink)}
.num-lines{display:grid;grid-template-columns:1fr 1fr;column-gap:16px;row-gap:3px}
.num-lines div{display:flex;gap:2px;align-items:flex-end}
.num-lines div span{flex:1;border-bottom:0.6px dashed rgba(255,255,255,.8);height:6px}
.side-word{position:absolute;left:2px;width:14px;display:flex;flex-direction:column;justify-content:space-around;align-items:center;font-size:7px;font-weight:700;color:var(--ink);line-height:1}
</style>
</head>
<body>

<div class="page-number" style="left:115px;top:2px">1</div>
<div class="page-number" style="left:406px;top:2px">2</div>
<div class="page-number" style="left:695px;top:2px">3</div>
<div class="page-number" style="left:1006px;top:2px">4</div>
<div class="page-number" style="left:118px;top:468px">5</div>
<div class="page-number" style="left:435px;top:468px">6</div>
<div class="page-number" style="left:718px;top:468px">7</div>
<div class="page-number" style="left:1026px;top:468px">8</div>

<!-- Cover -->
<section class="page cover" style="left:0;top:40px;width:288px;height:400px">
  <div class="brand" style="left:62px;top:20px">
    <div class="brand-dot"></div>
    <div class="brand-name">Lanternway 7.5</div>
  </div>
  <div class="art" role="img" aria-label="Illustration of a glowing light bulb rising from an open book surrounded by school icons and a red pencil" style="left:10px;top:62px;width:268px;height:296px;background:radial-gradient(circle at 50% 45%,#e6f7ff 0,#9fd6ea 28%,#5fb9a8 55%,var(--teal) 75%)"></div>
  <div class="abs" style="left:0;top:368px;width:288px;text-align:center;font-size:6px">To Inspire, Foster and Support Tomorrow's<br>Leaders and Innovators Today!</div>
</section>

<!-- Teacher pack -->
<section class="page teacher" style="left:291px;top:40px;width:289px;height:400px">
  <div class="abs" style="left:0;top:0;width:289px;height:92px;background:#fff"></div>
  <div class="abs dark" style="left:12px;top:18px;width:96px;text-align:center;font-size:6px">The T-Pack (Teacher)<br>The Lanternway 7.5 Your<br>Project-Launching</div>
  <div class="abs dark" style="left:18px;top:52px;font-size:14px;font-weight:800;text-decoration:underline;font-family:Oswald,sans-serif">Workshop</div>
  <div class="art" role="img" aria-label="Word cloud of education terms: knowledge, training, skills, goal, teaching" style="left:112px;top:0;width:177px;height:92px;background:linear-gradient(135deg,#1a1a1a,#2b2b2b 60%,#3a3320)"></div>

  <div class="art" role="img" aria-label="Me and We graphic" style="left:6px;top:100px;width:40px;height:32px;background:#b86a9a"></div>
  <div class="abs" style="left:52px;top:100px;width:230px">
    <div>(5 min)</div>
    <div class="h-sub" style="text-align:center;text-decoration:underline">1. Me and We</div>
    <div><b>ME</b> Participants identify resources and abilities they already possess.</div>
    <div><b>Objectives</b>&nbsp; 1) Share and appreciate individual abilities and talents<br>&nbsp;&nbsp;&nbsp;&nbsp;&nbsp;&nbsp;&nbsp;&nbsp;&nbsp;&nbsp;&nbsp;&nbsp;&nbsp;&nbsp;&nbsp;&nbsp;2) Recognize skills and talents of others</div>
    <div style="margin-top:3px">(10 min)<br><b>WE</b> Participants record each group member's abilities to create a resource pool.</div>
    <div><b>Objectives</b>&nbsp; 1) Highlight past experiences and achievements<br>&nbsp;&nbsp;&nbsp;&nbsp;&nbsp;&nbsp;&nbsp;&nbsp;&nbsp;&nbsp;&nbsp;&nbsp;&nbsp;&nbsp;&nbsp;&nbsp;2) Validate and identify individual strengths and knowledge</div>
  </div>
  <div class="art" role="img" aria-label="Brain made of gears" style="left:6px;top:178px;width:40px;height:32px;background:#6b3c64"></div>
  <div class="abs" style="left:52px;top:178px;width:230px">
    <div>(20 min)</div>
    <div class="h-sub" style="text-align:center;text-decoration:underline">2. The Brainstorm</div>
    <div>Participants identify 10 project ideas.</div>
    <div><b>Optional:</b> You can specify whether the project must fit into a specific subject category or designed for a particular purpose like "earth day" or to address a particular problem in the school or community. You decide.</div>
    <div><b>Objectives</b>&nbsp; 1) Recognize opportunities<br>&nbsp;&nbsp;&nbsp;&nbsp;&nbsp;&nbsp;&nbsp;&nbsp;&nbsp;&nbsp;&nbsp;&nbsp;&nbsp;&nbsp;&nbsp;&nbsp;2) Learn that ideas and abilities are marketable and of use to others.</div>
  </div>
  <div class="art" role="img" aria-label="Best of the Best title graphic with megaphone" style="left:6px;top:250px;width:46px;height:40px;background:var(--mint)"></div>
  <div class="abs" style="left:58px;top:250px;width:224px">
    <div>(10 min)</div>
    <div class="h-sub" style="text-align:center;text-decoration:underline">3. The Best of the Best</div>
    <div>Participants select the best project idea and create a task list.</div>
    <div><b>Objectives</b>&nbsp; 1) Evaluate and prioritize project ideas based on feasibility and value.<br>&nbsp;&nbsp;&nbsp;&nbsp;&nbsp;&nbsp;&nbsp;&nbsp;&nbsp;&nbsp;&nbsp;&nbsp;&nbsp;&nbsp;&nbsp;&nbsp;2) Begin the planning process</div>
  </div>
  <div class="art" role="img" aria-label="Big Pitch title graphic" style="left:6px;top:326px;width:46px;height:46px;background:#e8f6ff"></div>
  <div class="abs" style="left:58px;top:318px;width:224px">
    <div class="h-sub" style="text-align:center;text-decoration:underline">4. The Big Pitch</div>
    <div>(5 min)<br><b>Prepare</b><br>Participants list the positive points and challenges regarding the project.</div>
    <div style="margin-top:3px"><b>Objectives</b>&nbsp; 1) Identify potential selling points and to strengthen<br>&nbsp;&nbsp;&nbsp;&nbsp;&nbsp;&nbsp;&nbsp;&nbsp;&nbsp;&nbsp;&nbsp;&nbsp;&nbsp;&nbsp;&nbsp;&nbsp;project development skills<br>&nbsp;&nbsp;&nbsp;&nbsp;&nbsp;&nbsp;&nbsp;&nbsp;&nbsp;&nbsp;&nbsp;&nbsp;&nbsp;&nbsp;&nbsp;&nbsp;2) Recognize the value of a project and increase appreciation<br>&nbsp;&nbsp;&nbsp;&nbsp;&nbsp;&nbsp;&nbsp;&nbsp;&nbsp;&nbsp;&nbsp;&nbsp;&nbsp;&nbsp;&nbsp;&nbsp;and attachment to it</div>
  </div>
</section>

<!-- Teacher pack continued -->
<section class="page teacher-cont dark" style="left:582px;top:40px;width:291px;height:400px">
  <div class="abs" style="left:6px;top:4px;width:280px"><b>Present</b> (4-5 min per group)<br>per group Participants present and defend their project idea to the other groups. Members from other groups ask questions to clarify and critique each presentation. Teacher animates the exchange to keep order and keep questions/comments.</div>
  <div class="abs" style="left:6px;top:52px"><b>Objectives</b>&nbsp; 1) Improve presentation skills<br>&nbsp;&nbsp;&nbsp;&nbsp;&nbsp;&nbsp;&nbsp;&nbsp;&nbsp;&nbsp;&nbsp;&nbsp;&nbsp;&nbsp;&nbsp;&nbsp;2) Fine-tune project planning by collecting more opinions and observations</div>
  <div class="abs" style="left:84px;top:82px">(10 min)</div>
  <div class="abs h-sec" style="left:90px;top:90px;width:190px;color:var(--ink)">5. Launch Your Project!</div>
  <div class="art" role="img" aria-label="Head silhouette with light bulb and icons" style="left:8px;top:88px;width:48px;height:48px;background:var(--mint)"></div>
  <div class="abs" style="left:70px;top:104px;width:210px;text-align:center"><div class="h-sub">The Who's Who?</div><b>Participants match each group member with a profile description to determine which position or committee is best for each member.</b></div>
  <div class="abs" style="left:6px;top:158px"><b>Objectives</b>&nbsp; 1) Discover traits and talents as perceived by one's self and by one's peers.<br>&nbsp;&nbsp;&nbsp;&nbsp;&nbsp;&nbsp;&nbsp;&nbsp;&nbsp;&nbsp;&nbsp;&nbsp;&nbsp;&nbsp;&nbsp;&nbsp;2) Learn that each member's abilities are valuable in the realization of any project.<br>&nbsp;&nbsp;&nbsp;&nbsp;&nbsp;&nbsp;&nbsp;&nbsp;&nbsp;&nbsp;&nbsp;&nbsp;&nbsp;&nbsp;&nbsp;&nbsp;3) Validate and highlight characteristics that are often taken for granted.</div>
  <div class="abs" style="left:6px;top:188px"><b>The G-Pack!</b><br>Distribute one G-Pack to each group.<br>These optional tools will help students autonomously plan and implement their project.</div>
  <div class="abs" style="left:6px;top:218px"><b>Objectives</b>&nbsp; 1) Set the scene for participants to take responsibility for their project.</div>
  <div class="mint-box" style="left:8px;top:246px;width:88px;height:66px"><b>The Launch Continues</b>The implementation of the projects is an ongoing process. The teacher's role is to provide continued support and motivation.</div>
  <div class="mint-box" style="left:100px;top:246px;width:88px;height:66px"><b>Timeline</b>Tell the participants how much time they have to accomplish their project. Do the projects have to take place during a particular time period or event or by a certain deadline?</div>
  <div class="mint-box" style="left:192px;top:246px;width:90px;height:66px"><b>Frequency</b>Tell participants when they will be able to work on the project in class. Ex. The first 30 minutes of each period, one class per week, every class for a few weeks, etc.</div>
  <div class="mint-box" style="left:8px;top:322px;width:138px;height:62px"><b>Updates</b>Get progress reports from the project managers (Chameleons). Remind them that their job is to motivate their team and keep track of what people are doing. They should not be "doing everything".</div>
  <div class="mint-box" style="left:150px;top:322px;width:132px;height:62px"><b>The Goal</b>In times of difficulty, remind them their goal is to make something happen, even if it is not what they originally planned or had in mind. Our goal is to teach them to adapt their approaches and plans and ultimately succeed.</div>
</section>

<!-- Student: Me and We / Brainstorm -->
<section class="page student-one" style="left:878px;top:40px;width:322px;height:400px">
  <div class="art" role="img" aria-label="Me and We graphic" style="left:8px;top:6px;width:70px;height:58px;background:#b86a9a"></div>
  <div class="abs h-sec" style="left:150px;top:6px;width:160px">1. Me and We</div>
  <div class="abs" style="left:104px;top:20px;width:212px"><b>Me</b><br>List some of your talents, abilities, and interests. Think about private classes, sports, hobbies, music, computers, things you like, things you know how to do.</div>
  <div class="abs" style="left:104px;top:40px;width:210px;display:grid;grid-template-columns:1fr 1fr;column-gap:14px;row-gap:2px">
    <div class="rule"></div><div class="rule"></div><div class="rule"></div><div class="rule"></div><div class="rule"></div><div class="rule"></div><div class="rule"></div><div class="rule"></div>
  </div>
  <div class="abs" style="left:12px;top:98px"><b>We</b><br>List the talents, abilities, and interests of each of your group members.</div>
  <div class="mint-box" style="left:12px;top:118px;width:64px;height:50px">Name</div>
  <div class="mint-box" style="left:82px;top:118px;width:64px;height:50px">Name</div>
  <div class="mint-box" style="left:152px;top:118px;width:64px;height:50px">Name</div>
  <div class="mint-box" style="left:222px;top:118px;width:64px;height:50px">Name</div>
  <div class="art" role="img" aria-label="Brain made of gears" style="left:12px;top:180px;width:70px;height:58px;background:#6b3c64"></div>
  <div class="abs h-sec" style="left:150px;top:182px;width:160px">2. The Brainstorm</div>
  <div class="abs" style="left:118px;top:198px;width:196px"><b style="font-size:5.5px">Find some project ideas!<br>Here are 3 easy ways to do it!</b><br><br>1) Use what you wrote in part 1 to give you ideas!<br>2) What does your school need, what problems could you solve,<br>&nbsp;&nbsp;&nbsp;&nbsp;what would be great to have?<br>3) These categories might help!</div>
  <table class="abs" style="left:12px;top:280px;width:294px;background:var(--mint)">
    <tr><td>1) Education</td><td>2) Environment</td><td>3) Health</td><td>4) Entertainment</td><td>5) Sports</td></tr>
    <tr><td>6) Relationship building</td><td>7) Arts</td><td>8) Media</td><td>9) Social Justice</td><td>10) Technology</td></tr>
  </table>
  <div class="abs" style="left:12px;top:310px;font-weight:700">List activities, businesses, products, or services that would work well in your school or community.</div>
  <div class="abs num-lines" style="left:14px;top:320px;width:290px">
    <div>1.<span></span></div><div>6.<span></span></div><div>2.<span></span></div><div>7.<span></span></div><div>3.<span></span></div><div>8.<span></span></div><div>4.<span></span></div><div>9.<span></span></div><div>5.<span></span></div><div>10.<span></span></div>
  </div>
</section>

<!-- Student: Launch / Who Does What -->
<section class="page student-two" style="left:12px;top:515px;width:288px;height:400px">
  <div class="art" role="img" aria-label="Head silhouette with light bulb and icons" style="left:10px;top:6px;width:50px;height:50px;background:var(--mint)"></div>
  <div class="abs h-sec" style="left:110px;top:6px;width:170px">5. Launch The Project!</div>
  <div class="abs h-sub" style="left:100px;top:22px;font-size:9px">The Who's Who?</div>
  <div class="abs" style="left:100px;top:36px;width:180px">These are positions that are played in any project or business.<br>Read each description. Match each of your group members (including you) with the position that fits best.</div>
  <div class="abs" style="left:8px;top:70px;width:272px;line-height:1.5">
    <div><b>The Go-Getters</b> Public relations and sales These people like to talk and get people's attention. "Why be shy?" They promote and sell. <span style="display:inline-block;width:90px;border-bottom:.6px solid #fff"></span></div>
    <div><b>The Number-Crunchers</b> Finance and Administration These people are organized and can keep track of money and information. <span style="display:inline-block;width:90px;border-bottom:.6px solid #fff"></span></div>
    <div><b>The Doers</b> Production or Service provider If it's a product- they'll make it. If it's a service- they'll provide it. You can count on them! <span style="display:inline-block;width:60px;border-bottom:.6px solid #fff"></span></div>
    <div><b>The Magicians</b> Advertising and Publicity They have creative ideas. They come up with cool advertisements, slogans, and posters. <span style="display:inline-block;width:70px;border-bottom:.6px solid #fff"></span></div>
    <div><b>The Chameleon</b> Project manager They keep track of everything that needs to be done and who needs to do it! <span style="display:inline-block;width:70px;border-bottom:.6px solid #fff"></span></div>
  </div>
  <div class="abs" style="left:8px;top:160px;width:80px"><b>GO</b><br><b>You have a great project idea.<br>Now make it happen.</b></div>
  <div class="abs" style="left:104px;top:166px;width:90px"><b>Your idea will probably change.<br>Just keep moving forward.</b></div>
  <div class="abs" style="left:200px;top:160px;width:84px"><b>The G-Pack</b><br><b>Use the tools in it to help you.</b></div>
  <div class="abs" style="left:0;top:192px;width:288px;height:96px;background:linear-gradient(90deg,#fffbe0,#f7f2c4)"></div>
  <div class="art" role="img" aria-label="Team structure icon" style="left:8px;top:200px;width:62px;height:54px;background:#d9e4f2"></div>
  <div class="abs h-sec dark" style="left:110px;top:198px;width:170px;font-size:8.5px">Who Does What?</div>
  <div class="abs dark" style="left:82px;top:214px;width:200px"><b>You can use the 'Who Does What?' in two ways.</b><br><br>1) Make and update a list of all the things the whole group needs to do.<br><br>2) Each person in the group can use it to keep track of everything that needs to be done in their "committee". Ex. Marketing, fund-raising, production.</div>
  <table class="abs" style="left:8px;top:298px;width:272px;background:var(--mint)">
    <tr><th style="background:var(--green);width:34%">Task</th><th style="background:var(--orange);width:33%">Who will do it?</th><th style="background:var(--purple);color:#fff">When will you do it?</th></tr>
    <tr><td></td><td></td><td></td></tr><tr><td></td><td></td><td></td></tr><tr><td></td><td></td><td></td></tr><tr><td></td><td></td><td></td></tr><tr><td></td><td></td><td></td></tr><tr><td></td><td></td><td></td></tr><tr><td></td><td></td><td></td></tr><tr><td></td><td></td><td></td></tr><tr><td></td><td></td><td></td></tr><tr><td></td><td></td><td></td></tr>
  </table>
</section>

<!-- Student: Best of the Best / Big Pitch -->
<section class="page student-three" style="left:305px;top:515px;width:287px;height:400px">
  <div class="abs h-sec" style="left:110px;top:6px;width:170px">3. The Best of the Best</div>
  <div class="art" role="img" aria-label="Best of the Best title graphic with megaphone" style="left:6px;top:20px;width:82px;height:68px;background:var(--mint)"></div>
  <div class="abs" style="left:102px;top:26px;width:180px;line-height:1.7">Choose your best idea or combine some to make one!<br>Is your idea realistic, original, and useful?<br>Project Idea or Name: <span style="display:inline-block;width:90px;border-bottom:.6px solid #fff"></span><br>Tasks: List all the things you'd have to do to make this project happen.<br><br>Think about money, permission, production, materials, promotion, everything!</div>
  <div class="abs num-lines" style="left:12px;top:98px;width:268px;row-gap:5px">
    <div>1.<span></span></div><div>6.<span></span></div><div>2.<span></span></div><div>7.<span></span></div><div>3.<span></span></div><div>8.<span></span></div><div>4.<span></span></div><div>9.<span></span></div><div>5.<span></span></div><div>10.<span></span></div>
  </div>
  <div class="abs h-sec" style="left:110px;top:164px;width:170px">4. The Big Pitch</div>
  <div class="art" role="img" aria-label="Big Pitch title graphic" style="left:6px;top:176px;width:80px;height:70px;background:#e8f6ff"></div>
  <div class="abs" style="left:100px;top:178px;width:182px">Prepare<br>List all the positive points and all the challenges you may have in doing this project.</div>
  <div class="abs" style="left:104px;top:204px;width:80px;text-align:center">Positive Points</div>
  <div class="abs" style="left:196px;top:204px;width:80px;text-align:center">Challenges</div>
  <div class="abs" style="left:100px;top:212px;width:84px;line-height:1.4">1.<div class="rule" style="display:inline-block;width:70px"></div><br>2.<div class="rule" style="display:inline-block;width:70px"></div><br>3.<div class="rule" style="display:inline-block;width:70px"></div><br>4.<div class="rule" style="display:inline-block;width:70px"></div><br>5.<div class="rule" style="display:inline-block;width:70px"></div></div>
  <div class="abs" style="left:194px;top:212px;width:84px;line-height:1.4">1.<div class="rule" style="display:inline-block;width:70px"></div><br>2.<div class="rule" style="display:inline-block;width:70px"></div><br>3.<div class="rule" style="display:inline-block;width:70px"></div><br>4.<div class="rule" style="display:inline-block;width:70px"></div><br>5.<div class="rule" style="display:inline-block;width:70px"></div></div>
  <div class="abs" style="left:8px;top:270px;width:272px"><b>Present!</b><br>Two or more members of your team will present your project to the other groups. Your presentation should answer these questions in an interesting, fun, or original way! If you have time, make a poster with a visual of your slogan, logo, or ad.</div>
  <div class="abs" style="left:8px;top:300px;width:260px;line-height:1.5">
    1) Where did your idea come from?<div class="rule"></div>
    2) What is the idea and what will have to be done?<div class="rule"></div>
    3) Why is this a good idea?<div class="rule"></div>
    4) Who will benefit from your project?<div class="rule"></div>
  </div>
  <div class="abs" style="left:8px;top:380px;width:272px">All the other teams will look for missing details, ask questions, find problems, and offer suggestions! So be ready to defend your idea!</div>
</section>

<!-- Group pack: Money Machines -->
<section class="page money" style="left:595px;top:515px;width:292px;height:400px">
  <div class="abs" style="left:0;top:0;width:292px;height:80px;background:linear-gradient(180deg,#fffde8,#f1f6d0)"></div>
  <div class="art" role="img" aria-label="Stacks of banknotes and coins" style="left:4px;top:8px;width:80px;height:56px;background:linear-gradient(135deg,#9ac86a,#4f8f3f)"></div>
  <div class="abs h-sec dark" style="left:100px;top:10px;width:170px">The Money Machines</div>
  <div class="abs dark" style="left:96px;top:24px;width:190px"><b style="font-size:6px">FINANCIAL NEEDS</b><br>Make money your friend- not your enemy! You've got to know what you need and how much it costs! Ex. Doers realize that they will need 6 soccer-balls, 100 drinks 2 referee sweaters, etc.</div>
  <div class="abs dark" style="left:96px;top:64px">Project name: <span style="display:inline-block;width:60px;border-bottom:.6px solid var(--ink)"></span>&nbsp;&nbsp;&nbsp;&nbsp; Date: <span style="display:inline-block;width:50px;border-bottom:.6px solid var(--ink)"></span></div>

  <div class="abs" style="left:12px;top:94px;width:270px;height:116px;background:#fff">
    <div class="side-word" style="top:6px;height:104px"><span>I</span><span>N</span><span>C</span><span>O</span><span>M</span><span>E</span></div>
    <table class="abs" style="left:18px;top:4px;width:248px;background:var(--mint)">
      <tr><th>Item</th><th>Amount</th><th>Total</th></tr>
      <tr><td>Sponsorships or Donations</td><td></td><td>$ 500</td></tr>
      <tr><td>School Help</td><td></td><td>$ 50</td></tr>
      <tr><td>Sales</td><td></td><td>$ 100</td></tr>
      <tr><td></td><td></td><td></td></tr><tr><td></td><td></td><td></td></tr><tr><td></td><td></td><td></td></tr><tr><td></td><td></td><td></td></tr><tr><td></td><td></td><td></td></tr><tr><td></td><td></td><td></td></tr>
      <tr><td>***************</td><td></td><td><b>Total $ Needed</b></td></tr>
    </table>
  </div>
  <div class="abs" style="left:12px;top:220px;width:270px;height:106px;background:#fff">
    <div class="side-word" style="top:4px;height:98px"><span>E</span><span>X</span><span>P</span><span>E</span><span>N</span><span>S</span><span>E</span><span>S</span></div>
    <table class="abs" style="left:18px;top:4px;width:248px;background:var(--mint)">
      <tr><th>Item</th><th>Quantity</th><th>Cost</th><th>Total</th></tr>
      <tr><td>Soccer balls</td><td>6</td><td>Free from school</td><td>$ 0</td></tr>
      <tr><td>Drinks</td><td>100</td><td>50 cents</td><td>$ 50</td></tr>
      <tr><td></td><td></td><td></td><td></td></tr><tr><td></td><td></td><td></td><td></td></tr><tr><td></td><td></td><td></td><td></td></tr><tr><td></td><td></td><td></td><td></td></tr><tr><td></td><td></td><td></td><td></td></tr><tr><td></td><td></td><td></td><td></td></tr>
      <tr><td>***************</td><td>***************</td><td><b>Total $ Needed</b></td><td></td></tr>
    </table>
  </div>
  <div class="abs" style="left:12px;top:336px;width:270px;height:52px;background:#fff">
    <div class="side-word" style="top:3px;height:46px;font-size:6.5px"><span>T</span><span>O</span><span>T</span><span>A</span><span>L</span></div>
    <table class="abs" style="left:18px;top:4px;width:248px;background:var(--mint)">
      <tr><th>Item</th><th>Amount</th><th>Total</th></tr>
      <tr><td>Income</td><td></td><td></td></tr>
      <tr><td>Expenses</td><td></td><td></td></tr>
      <tr><td><b>(Total 1 – Total 2)</b></td><td><b>Total $ Needed</b></td><td></td></tr>
    </table>
  </div>
</section>

<!-- Group pack: sponsor letter -->
<section class="page letter" style="left:887px;top:515px;width:313px;height:400px">
  <div class="abs" style="left:8px;top:6px;width:296px;line-height:1.45">
    DATE<br><br>Dear Mr./Ms. Name,<br><br>
    We sincerely appreciate Company or Organization's Name dedication to supporting youth initiatives in the community and are thankful for the opportunity to submit our donation request! We at School/Org Name are hoping to help, promote and support our cause by Organizing /Launching/Etc. a Project Name in our local community. With this in mind, we are currently seeking donations and/or sponsorships which would aid our effort. Our project will focus on Describe Project Target &amp; Objectives.<br><br>
    We sincerely feel that you would be a great fit with our initiative and are respectfully requesting Donation Amount/Materials.<br><br><br>
    <b>Project/Event Details</b><br><br><b>Project Name:</b><br><b>Location of Event:</b><br><br>
    Your support would be an invaluable partnership and your donation will directly impact our goal! Thank you and please feel free to reach out if you have any additional questions about the project or our organization.<br><br>
    Kind regards,<br><br><b>Your Name</b><br><br>School or Organization Name<br>Your Phone Number<br>Your Email
  </div>
  <div class="abs" style="left:0;top:246px;width:313px;height:154px;background:var(--teal-dark);opacity:.35"></div>
  <div class="abs" style="left:0;top:252px;width:313px;text-align:center;font-size:5.5px"><span style="text-decoration:underline">Address</span><br><b>18 Orchard Lane, Suite 4B,<br>Brookfield, ON K2P 0A1, Canada</b></div>
  <div class="abs" style="left:40px;top:300px;font-size:5.5px">Call Us: 555-014-2290</div>
  <div class="abs" style="left:176px;top:300px;font-size:5.5px">Email: hello@lanternway.example</div>
  <div class="brand" style="left:64px;top:342px">
    <div class="brand-dot" style="width:30px;height:30px"></div>
    <div class="brand-name" style="font-size:18px">Lanternway 7.5</div>
  </div>
</section>

</body>
</html>
```